Business Card Design Project

I want my business cards to stand and feel timeless! I also want people to get their hands on them and freak out over how cool these are, I already have a logo i just want a very cool card design! this is for a makeup artist and maybe one day a line of cosmetics.

Target Market(s)

I want this to target women from 18 to 45

Industry/Entity Type

Business

Font styles to use
Decorative
Script

Colors

Designer to choose colors to be used in the design.

Requirements
Must have
• it must be elegante

```html
<!DOCTYPE html>
<html lang="en">
<head>
<meta charset="utf-8">
<title>Mira Lane Business Card</title>
<link href="https://fonts.googleapis.com/css2?family=Julius+Sans+One&family=Montserrat:wght@400;500&display=swap" rel="stylesheet">
<style>
  :root {
    --page: #1b1b1e;
    --card: #2e2d32;
    --logo: #56555c;
    --frame: #2f6a8e;
    --band: #285a79;
    --tile: #222126;
    --text: #e6e6ea;
    --muted: #9aa7b2;
  }
  * { box-sizing: border-box; margin: 0; padding: 0; }
  html, body {
    width: 1200px; height: 4018px; overflow: hidden;
    background: var(--page);
    font-family: "Montserrat", sans-serif;
  }
  .sheet {
    width: 1200px; height: 4018px;
    display: flex; flex-direction: column; align-items: center; justify-content: center;
    gap: 200px;
  }
  .card {
    position: relative; width: 1000px; height: 572px;
    background: var(--card);
    box-shadow: 0 20px 50px rgba(0,0,0,.45);
    overflow: hidden;
  }
  .wordmark {
    font-family: "Julius Sans One", sans-serif;
    color: var(--logo);
    font-size: 64px; letter-spacing: 6px; line-height: 1;
    text-align: center;
  }
  .wordmark .tagline {
    display: block; margin-top: 10px;
    font-family: "Montserrat", sans-serif;
    font-size: 12px; letter-spacing: 10px;
  }
  /* front */
  .front .frame {
    position: absolute; left: 90px; top: 70px; right: 90px; bottom: 70px;
    border: 2px solid var(--frame);
  }
  .front .wordmark {
    position: absolute; left: 0; right: 0; top: 220px;
  }
  .front .website {
    position: absolute; left: 50%; bottom: 58px; transform: translateX(-50%);
    background: var(--card); padding: 0 22px;
    color: var(--text); font-size: 17px; letter-spacing: 7px;
  }
  /* back */
  .back .wordmark {
    position: absolute; left: 70px; top: 330px; text-align: left; font-size: 58px;
  }
  .back .nameband {
    position: absolute; left: 540px; right: 0; top: 110px; height: 96px;
    background: var(--band);
    padding: 16px 0 0 34px;
  }
  .nameband .name { color: var(--text); font-size: 30px; letter-spacing: 4px; font-weight: 500; }
  .nameband .role { color: var(--muted); font-size: 13px; letter-spacing: 8px; margin-top: 6px; }
  .back .contacts {
    position: absolute; left: 540px; top: 236px;
    border-left: 2px solid var(--tile);
    padding-left: 0;
    display: flex; flex-direction: column; gap: 18px;
  }
  .contact { display: flex; align-items: flex-start; gap: 18px; }
  .contact .icon {
    width: 40px; height: 40px; background: var(--tile);
    display: flex; align-items: center; justify-content: center; flex: none;
  }
  .contact .value { color: var(--text); font-size: 19px; letter-spacing: 1.5px; line-height: 1.3; padding-top: 8px; }
  .contact .value.phone { font-size: 26px; letter-spacing: 4px; padding-top: 3px; }
</style>
</head>
<body>
<main class="sheet">
  <section class="card front">
    <div class="frame"></div>
    <div class="wordmark">MIRALANE<span class="tagline">MAKEUP ARTIST</span></div>
    <div class="website">www.miralane.com</div>
  </section>

  <section class="card back">
    <div class="wordmark">MIRALANE<span class="tagline">MAKEUP ARTIST</span></div>
    <div class="nameband">
      <div class="name">Evan Hale</div>
      <div class="role">DIRECTOR</div>
    </div>
    <div class="contacts">
      <div class="contact">
        <span class="icon"><svg width="22" height="22" viewBox="0 0 24 24"><path fill="#e6e6ea" d="M6.6 10.8a15 15 0 0 0 6.6 6.6l2.2-2.2a1 1 0 0 1 1-.25 11.4 11.4 0 0 0 3.6.57 1 1 0 0 1 1 1V20a1 1 0 0 1-1 1A17 17 0 0 1 3 4a1 1 0 0 1 1-1h3.5a1 1 0 0 1 1 1c0 1.25.2 2.45.57 3.57a1 1 0 0 1-.25 1z"/></svg></span>
        <span class="value phone">04 18 36 90</span>
      </div>
      <div class="contact">
        <span class="icon"><svg width="22" height="22" viewBox="0 0 24 24"><rect x="3" y="6" width="18" height="12" fill="#e6e6ea"/><path d="M3 6l9 7 9-7" fill="none" stroke="#222126" stroke-width="1.6"/></svg></span>
        <span class="value">evan@mail.com</span>
      </div>
      <div class="contact">
        <span class="icon"><svg width="22" height="22" viewBox="0 0 24 24"><path fill="#e6e6ea" d="M12 3l9 8h-3v9h-4v-6h-4v6H6v-9H3z"/></svg></span>
        <span class="value">42 Rowan Street<br>Leeds, 60418</span>
      </div>
    </div>
  </section>
</main>
</body>
</html>
```